upmarket Hair salon A5 flyer design colour double sided

Phone number 9318 7061
address is shop 3/7 Marlowe pde Larkfield
Hi i am wanting a flyer that is upmarket and elegant for my hair salon Velvet Strands For Hair if any pics of hair must look great.
both side must have logo and contact details on
offer side 1
50% off
style cut and finish
*not valid Saturdays
*expires 31/03/15
*butler salon only
*not valid with any other offers
offer side 2
1/2 head foils or all over colour,
cut and finish
$120
*toners and treatment extra costs
*expires 31/03/15
*butler salon only

```html
<!DOCTYPE html>
<html lang="en">
<head>
<meta charset="utf-8">
<title>Velvet Strands – Salon Offers</title>
<link rel="stylesheet" href="https://fonts.googleapis.com/css2?family=Cormorant+Garamond:ital,wght@0,400;0,500;1,400;1,500&family=Lato:wght@400&display=swap">
<style>
  :root {
    --teal: #2f9a98;
    --ink: #1a1a1a;
    --text: #2b2b2b;
    --white: #ffffff;
    --grey-light: #ececec;
    --rule: #cfe3e3;
  }
  * { box-sizing: border-box; margin: 0; padding: 0; }
  html, body { width: 909px; height: 1200px; overflow: hidden; background: var(--white); }
  .flyer { position: relative; width: 909px; height: 1200px; font-variant-numeric: lining-nums; }
  .flyer-side { position: relative; width: 909px; height: 600px; overflow: hidden; background: var(--white); }
  .flyer-side + .flyer-side { border-top: 1px solid var(--rule); }
  .side-art { position: absolute; inset: 0; width: 909px; height: 600px; }

  .brand { position: absolute; left: 596px; top: 56px; width: 290px; }
  .brand-name {
    font-family: "Cormorant Garamond", serif; font-style: italic; font-weight: 500;
    font-size: 42px; line-height: 1; color: var(--ink); letter-spacing: 0.5px;
  }
  .brand-tagline {
    margin-top: 24px; padding-left: 38px;
    font-family: "Lato", sans-serif; font-size: 14.5px; color: #3a3a3a;
  }

  .offer-tag {
    position: absolute; border-radius: 50%;
    background: var(--ink); display: flex; flex-direction: column;
    align-items: center; justify-content: center; text-align: center;
    font-family: "Cormorant Garamond", serif; color: var(--white);
    font-variant-numeric: lining-nums;
  }
  .offer-tag--discount { left: 448px; top: 229px; width: 160px; height: 160px; }
  .offer-tag--package { left: 442px; top: 243px; width: 170px; height: 170px; }
  .discount-figure { font-size: 46px; line-height: 1; font-weight: 500; white-space: nowrap; }
  .discount-figure sup { font-size: 24px; vertical-align: 16px; }
  .discount-off { font-style: italic; color: var(--teal); font-size: 22px; }
  .discount-detail { font-style: italic; font-size: 22px; line-height: 1.1; margin-top: 6px; }
  .package-detail { font-style: italic; color: var(--teal); font-size: 21px; line-height: 1.05; }
  .package-price { font-size: 42px; line-height: 1; margin-top: 12px; }

  .terms {
    position: absolute; left: 44px; top: 474px; list-style: none;
    font-family: "Cormorant Garamond", serif; font-style: italic; font-size: 20px;
    line-height: 26px; color: var(--text);
  }
  .terms li::before { content: "\2731"; color: var(--teal); font-style: normal; font-size: 12px; margin-right: 12px; position: relative; top: -2px; }

  .contact {
    position: absolute; left: 664px; top: 458px;
    font-family: "Cormorant Garamond", serif; font-style: italic; color: var(--text);
  }
  .contact-title { font-size: 27px; font-weight: 400; line-height: 1.2; }
  .contact-phone { margin-top: 6px; font-size: 15px; }
  .contact-phone strong { font-weight: 400; font-size: 25px; margin-left: 6px; }
  .contact-address { margin-top: 4px; font-size: 15px; line-height: 27px; }
</style>
</head>
<body>
<main class="flyer">

  <section class="flyer-side flyer-side--discount">
    <svg class="side-art" viewBox="0 0 909 600">
      <defs>
        <linearGradient id="greyBand" x1="0" y1="0" x2="1" y2="0">
          <stop offset="0" stop-color="#e8e8e9"/>
          <stop offset="0.6" stop-color="#d6d7d8"/>
          <stop offset="1" stop-color="#c4c5c6"/>
        </linearGradient>
        <linearGradient id="photoTonesA" x1="0" y1="0" x2="1" y2="0">
          <stop offset="0" stop-color="#b6a79a"/>
          <stop offset="0.35" stop-color="#c59a78"/>
          <stop offset="0.7" stop-color="#e6ddd6"/>
          <stop offset="1" stop-color="#e8e8e9" stop-opacity="0"/>
        </linearGradient>
        <clipPath id="upperA"><path d="M0,0 H909 V175 C760,190 620,235 500,290 C380,345 200,350 0,290 Z"/></clipPath>
      </defs>
      <path d="M0,0 H909 V175 C760,190 620,235 500,290 C380,345 200,350 0,290 Z" fill="url(#greyBand)"/>
      <path d="M909,150 C800,160 720,185 640,215 L909,215 Z" fill="var(--grey-light)" opacity="0.7"/>
      <rect x="0" y="0" width="520" height="360" fill="url(#photoTonesA)" clip-path="url(#upperA)" role="img" aria-label="Photo: smiling woman with long brown hair being blow-dried and brushed by a stylist"/>
      <path d="M0,262 C60,300 130,330 210,345 C130,347 55,330 0,312 Z" fill="var(--ink)"/>
      <path d="M70,305 C250,335 420,315 560,262 C640,233 700,218 760,214 C640,262 520,322 360,346 C250,360 150,348 70,305 Z" fill="var(--teal)"/>
      <path d="M597,321 C640,330 690,345 670,362 C650,378 610,350 597,330" fill="none" stroke="var(--ink)" stroke-width="2"/>
      <path d="M605,370 C640,375 670,372 690,366" fill="none" stroke="#bbb" stroke-width="4" opacity="0.5"/>
      <circle cx="592" cy="320" r="7" fill="var(--ink)" stroke="var(--white)" stroke-width="2"/>
    </svg>

    <div class="brand">
      <div class="brand-name">Velvet Strands</div>
      <p class="brand-tagline">Beauty Care &amp; Hair Dressing</p>
    </div>

    <div class="offer-tag offer-tag--discount">
      <div class="discount-figure">50%<sup>*</sup><span class="discount-off">-off</span></div>
      <div class="discount-detail">style cut &amp;<br>finish</div>
    </div>

    <ul class="terms">
      <li>Not valid Saturdays</li>
      <li>Expires 31/03/15</li>
      <li>Larkfield salon only</li>
      <li>Not valid with any other offers</li>
    </ul>

    <div class="contact">
      <h2 class="contact-title">Contact details</h2>
      <p class="contact-phone">Phone <strong>9318 7061</strong></p>
      <p class="contact-address">Address is shop<br>3/7 Marlowe pde Larkfield</p>
    </div>
  </section>

  <section class="flyer-side flyer-side--package">
    <svg class="side-art" viewBox="0 0 909 600">
      <defs>
        <linearGradient id="beigeBand" x1="0" y1="0" x2="1" y2="0">
          <stop offset="0" stop-color="#e6e2dc"/>
          <stop offset="0.6" stop-color="#d3ccc2"/>
          <stop offset="1" stop-color="#c6beb2"/>
        </linearGradient>
        <linearGradient id="photoTonesB" x1="0" y1="0" x2="1" y2="0">
          <stop offset="0" stop-color="#d98a68"/>
          <stop offset="0.35" stop-color="#e2c39a"/>
          <stop offset="0.7" stop-color="#e6e0da"/>
          <stop offset="1" stop-color="#e6e2dc" stop-opacity="0"/>
        </linearGradient>
        <clipPath id="upperB"><path d="M0,0 H909 V175 C760,190 620,235 500,290 C380,345 200,350 0,290 Z"/></clipPath>
      </defs>
      <path d="M0,0 H909 V175 C760,190 620,235 500,290 C380,345 200,350 0,290 Z" fill="url(#beigeBand)"/>
      <path d="M909,150 C800,160 720,185 640,215 L909,215 Z" fill="var(--grey-light)" opacity="0.7"/>
      <rect x="0" y="0" width="520" height="360" fill="url(#photoTonesB)" clip-path="url(#upperB)" role="img" aria-label="Photo: woman with straight blonde hair while a stylist in orange uses a hair straightener"/>
      <path d="M0,262 C60,300 130,330 210,345 C130,347 55,330 0,312 Z" fill="var(--ink)"/>
      <path d="M70,305 C250,335 420,315 560,262 C640,233 700,218 760,214 C640,262 520,322 360,346 C250,360 150,348 70,305 Z" fill="var(--teal)"/>
      <path d="M613,313 C650,325 700,340 680,360 C660,376 620,345 613,323" fill="none" stroke="var(--ink)" stroke-width="2"/>
      <path d="M620,370 C650,376 680,372 700,366" fill="none" stroke="#bbb" stroke-width="4" opacity="0.5"/>
      <circle cx="607" cy="313" r="7" fill="var(--ink)" stroke="var(--white)" stroke-width="2"/>
    </svg>

    <div class="brand">
      <div class="brand-name">Velvet Strands</div>
      <p class="brand-tagline">Beauty Care &amp; Hair Dressing</p>
    </div>

    <div class="offer-tag offer-tag--package">
      <div class="package-detail">1/2 Head foils or<br>All over colour,<br>Cut and finish</div>
      <div class="package-price">$120</div>
    </div>

    <ul class="terms">
      <li>Toners and treatment extra costs</li>
      <li>Expires 31/03/15</li>
      <li>Larkfield salon only</li>
      <li>Not valid with any other offers</li>
    </ul>

    <div class="contact">
      <h2 class="contact-title">Contact details</h2>
      <p class="contact-phone">Phone <strong>9318 7061</strong></p>
      <p class="contact-address">Address is shop<br>3/7 Marlowe pde Larkfield</p>
    </div>
  </section>

</main>
</body>
</html>
```